Restaurant poster for inside

We are a fast food lebanese restaurant franchise that needs posters designed for our catering special for the month of Ramadan.
The special is buy 12, get 6 free. This offer is for all starters.
Our slogan for this special is "A part of your family!"
Should also have words "Ramadan Mubarak"
The design should aslo include a Lantern which is a symbol of Ramadan. The poster size is A0.
Somewhere on the poster is should state, This offer is only vaild during the month of Ramadan.
Muslims who are celebrating the ramadan holiday
Restaurant

```html
<!DOCTYPE html>
<html lang="en">
<head>
<meta charset="utf-8">
<title>Ramadan Mubarak – Starters Offer</title>
<link rel="stylesheet" href="https://fonts.googleapis.com/css2?family=Aladin&family=Roboto:wght@300;400;700&display=swap">
<style>
  :root {
    --bg-center: #3f63cc;
    --bg-mid: #2a44a8;
    --bg-edge: #1c2a86;
    --title-cyan: #2bb3ea;
    --buy-orange: #ea6f2b;
    --get-amber: #f4a63a;
    --free-yellow: #f8c033;
    --note-green: #a9c95b;
    --badge-blue: #2f86d6;
    --white: #ffffff;
    --lantern-a: #2fb0ec;
    --lantern-b: #1a8fd0;
    --plate-white: #f6f6f4;
    --food-light: #d9b27a;
    --food-mid: #b07840;
    --food-dark: #7a4a28;
  }
  html, body {
    margin: 0;
    padding: 0;
    width: 849px;
    height: 1200px;
    overflow: hidden;
    background: var(--bg-edge);
  }
  .poster {
    position: relative;
    width: 849px;
    height: 1200px;
    overflow: hidden;
    background: radial-gradient(ellipse 70% 60% at 55% 45%, var(--bg-center) 0%, var(--bg-mid) 55%, var(--bg-edge) 100%);
    font-family: "Roboto", Arial, sans-serif;
  }
  .greeting {
    position: absolute;
    top: 30px;
    left: 0;
    width: 849px;
    margin: 0;
    text-align: center;
    font-family: "Aladin", cursive;
    font-weight: 400;
    font-size: 78px;
    line-height: 1;
    color: var(--title-cyan);
    letter-spacing: 1px;
  }
  .lantern {
    position: absolute;
    left: 113px;
    top: 188px;
    width: 148px;
    height: 336px;
  }
  .offer {
    position: absolute;
    right: 115px;
    top: 0;
    margin: 0;
    text-align: right;
    font-weight: 300;
    line-height: 1;
  }
  .offer span { display: block; position: absolute; right: 0; white-space: nowrap; }
  .offer-buy  { top: 162px; font-size: 90px; color: var(--buy-orange); }
  .offer-get  { top: 249px; font-size: 124px; color: var(--get-amber); }
  .offer-free { top: 366px; font-size: 162px; color: var(--free-yellow); }
  .offer-note {
    position: absolute;
    right: 112px;
    top: 526px;
    margin: 0;
    font-weight: 300;
    font-size: 27px;
    color: var(--note-green);
    white-space: nowrap;
  }
  .platter {
    position: absolute;
    left: 0;
    top: 620px;
    width: 849px;
    height: 580px;
  }
  .slogan-badge {
    position: absolute;
    left: 491px;
    top: 590px;
    width: 272px;
    height: 262px;
    border-radius: 50%;
    border: 2px solid var(--white);
    background: rgba(47, 134, 214, 0.88);
    box-sizing: border-box;
    display: flex;
    align-items: center;
    justify-content: center;
    text-align: center;
    color: var(--white);
    font-weight: 300;
    font-size: 43px;
    line-height: 1.12;
    margin: 0;
  }
  .brand {
    position: absolute;
    left: 44px;
    top: 1060px;
    margin: 0;
    color: var(--white);
  }
  .brand-name {
    display: flex;
    align-items: center;
    gap: 10px;
    font-weight: 700;
    font-size: 44px;
    line-height: 1;
  }
  .brand-dot {
    width: 26px;
    height: 26px;
    border-radius: 50%;
    background: var(--white);
  }
  .brand-tagline {
    display: block;
    margin-top: 8px;
    font-weight: 700;
    font-size: 11px;
    letter-spacing: 3px;
    text-transform: uppercase;
  }
</style>
</head>
<body>
  <main class="poster">
    <h1 class="greeting">Ramadan Mubarak</h1>

    <svg class="lantern" viewBox="0 0 148 336" role="img" aria-label="Illustration of an ornate Ramadan lantern">
      <defs>
        <linearGradient id="lanternTone" x1="0" y1="0" x2="0" y2="1">
          <stop offset="0" stop-color="var(--lantern-a)"/>
          <stop offset="1" stop-color="var(--lantern-b)"/>
        </linearGradient>
      </defs>
      <rect x="0" y="0" width="148" height="336" rx="20" fill="url(#lanternTone)" opacity="0.85"/>
    </svg>

    <h2 class="offer">
      <span class="offer-buy">BUY 12</span>
      <span class="offer-get">GET 6</span>
      <span class="offer-free">FREE</span>
    </h2>
    <p class="offer-note">all starters in Ramadan</p>

    <svg class="platter" viewBox="0 0 849 580" role="img" aria-label="Photo of a white rectangular platter of Lebanese starters: vine leaves, falafel, pickled turnips, cheese rolls, kibbeh and fatayer">
      <defs>
        <linearGradient id="platterTone" x1="0.1" y1="0.2" x2="0.9" y2="0.8">
          <stop offset="0" stop-color="var(--plate-white)"/>
          <stop offset="0.3" stop-color="var(--food-light)"/>
          <stop offset="0.65" stop-color="var(--food-mid)"/>
          <stop offset="1" stop-color="var(--food-dark)"/>
        </linearGradient>
      </defs>
      <polygon points="16,172 292,32 828,303 556,556"
               fill="url(#platterTone)" stroke="var(--plate-white)" stroke-width="14" stroke-linejoin="round"/>
    </svg>

    <p class="slogan-badge">a part<br>of your<br>family!</p>

    <p class="brand">
      <span class="brand-name">Cedar Table <span class="brand-dot"></span></span>
      <span class="brand-tagline">Authentic Lebanese Food</span>
    </p>
  </main>
</body>
</html>
```